business cards mobile food bus

Mobile food bus fish& chips , burgers ,drinks . platters & catering events

Target Market(s)

general public

Industry/Entity Type

Catering

Contact Information for Business Card

Marla Quinby

Mobile 0431952876

Font styles to use
Sans Serif

Colors
1b1b1b
f37122

```html
<!DOCTYPE html>
<html lang="en">
<head>
<meta charset="utf-8">
<title>Mobile Food Bus – Business Card</title>
<link rel="stylesheet" href="https://fonts.googleapis.com/css2?family=Arimo:wght@400;700&display=swap">
<style>
  :root {
    --ink: #1b1b1b;
    --black: #050505;
    --orange: #f37122;
    --orange-deep: #d9560f;
    --white: #ffffff;
    --stage: #e9e6e2;
  }
  * { box-sizing: border-box; margin: 0; padding: 0; }
  html, body {
    width: 1200px; height: 1200px; overflow: hidden;
    background: var(--stage);
  }
  .card {
    position: absolute; left: 50px; top: 260px;
    width: 1100px; height: 680px;
    background: linear-gradient(to bottom, var(--black) 0%, var(--ink) 52%, #5a2a0c 72%, var(--orange-deep) 90%, var(--orange) 100%);
    box-shadow: 0 10px 30px rgba(0,0,0,.35);
    overflow: hidden;
  }
  .brand-title {
    position: absolute; left: 0; right: 0; top: 58px;
    text-align: center;
    font-family: "Arimo", sans-serif; font-weight: 700;
    font-size: 92px; letter-spacing: 2px; line-height: 1;
    color: var(--orange);
    white-space: nowrap;
  }
  .services {
    position: absolute; left: 0; right: 0; top: 168px;
    text-align: center;
    font-family: "Arimo", sans-serif; font-weight: 700;
    font-size: 25px; letter-spacing: 1px;
    color: var(--white);
    white-space: nowrap;
  }
  .gallery {
    position: absolute; left: 43px; top: 250px;
    display: flex; gap: 24px;
  }
  .photo {
    width: 238px; height: 265px;
    border: 3px solid var(--orange); border-radius: 14px;
  }
  .photo--platter { background: radial-gradient(circle at 50% 50%, #d9b27a 0%, #a8553a 55%, #7a1620 100%); }
  .photo--burger  { background: linear-gradient(to bottom, #6b4a2a 0%, #d99a4e 25%, #5a9a3a 48%, #c8361e 58%, #4a2a1a 72%, #e6b073 88%, #f2eee8 100%); }
  .photo--fish    { background: radial-gradient(circle at 60% 70%, #c7752a 0%, #b85f1f 40%, #6f8e3a 75%, #e3c98a 100%); }
  .photo--catering{ background: linear-gradient(to bottom, #8ea66a 0%, #e8e6e2 35%, #f4f2ef 60%, #b52a2a 100%); }
  .contact {
    position: absolute; top: 579px; height: 70px;
    display: flex; align-items: center; justify-content: center;
    background: linear-gradient(to bottom, #ffc15a 0%, #ffa030 45%, var(--orange) 70%, var(--orange-deep) 100%);
    border: 1px solid #ffd79a;
    box-shadow: 0 3px 6px rgba(0,0,0,.45);
    font-family: "Arimo", sans-serif; font-weight: 700;
    font-size: 36px; color: var(--ink); letter-spacing: .5px;
    white-space: nowrap;
  }
  .contact--name  { left: 43px;  width: 500px; }
  .contact--phone { left: 559px; width: 506px; }
</style>
</head>
<body>
  <div class="card">
    <h1 class="brand-title">MOBILE FOOD BUS</h1>
    <p class="services">FISH&amp; CHIPS | BURGERS | DRINKS | PLATTERS &amp; CATERING EVENTS</p>
    <div class="gallery">
      <div class="photo photo--platter" role="img" aria-label="Platter of wraps, sandwiches and grapes"></div>
      <div class="photo photo--burger" role="img" aria-label="Cheeseburger with lettuce and tomato"></div>
      <div class="photo photo--fish" role="img" aria-label="Battered fish with chips and salad"></div>
      <div class="photo photo--catering" role="img" aria-label="Long catering table set with plates and glasses"></div>
    </div>
    <div class="contact contact--name">MARLA QUINBY</div>
    <div class="contact contact--phone">MOBILE : 0431952876</div>
  </div>
</body>
</html>
```